Corporate Business Card

Very professional, Modern, Not to busy, include phone address email, website
(253) 555-0174, 61807 19th Street N, Kent, WA 98517, marcus@kestrelbayholding.com, brelvanindustries.com

Target Market(s)

Manufacturing

Industry/Entity Type

Aero, machining, manufacturing, Off road racing

Contact Information for Business Card

Phone, address email, website

```html
<!DOCTYPE html>
<html lang="en">
<head>
<meta charset="utf-8">
<title>Brelvan Industries – Business Card</title>
<link href="https://fonts.googleapis.com/css2?family=Montserrat:ital,wght@0,300;0,500;0,600;0,700;0,800;1,700&display=swap" rel="stylesheet">
<style>
  :root {
    --navy: #18356b;
    --red: #d2232a;
    --grey: #e4e5e7;
    --white: #ffffff;
    --stage: #eef0f4;
  }
  * { box-sizing: border-box; margin: 0; padding: 0; }
  html, body { width: 1200px; height: 1200px; overflow: hidden; }
  body {
    background: var(--stage);
    font-family: "Montserrat", Arial, sans-serif;
    color: var(--navy);
    position: relative;
  }
  .card {
    position: absolute;
    left: 205px;
    width: 790px;
    height: 450px;
    background: var(--white);
    border-radius: 30px;
    overflow: hidden;
    box-shadow: 0 18px 30px rgba(0, 0, 0, 0.18);
  }
  .card--front { top: 120px; }
  .card--back { top: 654px; }
  .card__shapes { position: absolute; inset: 0; width: 790px; height: 450px; }

  .wordmark { position: absolute; text-align: center; line-height: 1; }
  .wordmark__name {
    display: block;
    font-weight: 800;
    color: var(--navy);
    letter-spacing: 1px;
    text-transform: uppercase;
  }
  .wordmark__sub {
    display: block;
    font-weight: 800;
    color: var(--navy);
    text-transform: uppercase;
  }
  .card--front .wordmark { left: 0; width: 790px; top: 150px; }
  .card--front .wordmark__name { font-size: 66px; }
  .card--front .wordmark__sub { font-size: 24px; letter-spacing: 8px; margin-top: 14px; }
  .card--back .wordmark { left: 455px; width: 330px; top: 215px; }
  .card--back .wordmark__name { font-size: 48px; }
  .card--back .wordmark__sub { font-size: 18px; letter-spacing: 6px; margin-top: 10px; }

  .web-pill {
    position: absolute;
    left: 244px;
    top: 376px;
    width: 310px;
    height: 34px;
    line-height: 34px;
    text-align: center;
    color: var(--white);
    font-weight: 300;
    font-size: 16px;
    letter-spacing: 2px;
  }

  .holder { position: absolute; left: 0; top: 52px; width: 420px; height: 88px; }
  .holder__name {
    position: absolute; left: 67px; top: 12px;
    font-weight: 700; font-size: 31px; color: var(--white); letter-spacing: 0.5px;
  }
  .holder__name em { font-style: normal; color: var(--red); }
  .holder__role {
    position: absolute; left: 108px; top: 56px;
    display: flex; align-items: center; gap: 4px;
    font-weight: 700; font-style: italic; font-size: 13.5px; color: var(--white); letter-spacing: 1.2px;
  }
  .holder__rule { display: inline-block; width: 52px; height: 1.5px; background: var(--white); }
  .holder__rule--red { width: 14px; background: var(--red); margin-right: 2px; }

  .contacts { position: absolute; left: 43px; top: 175px; list-style: none; }
  .contact { display: flex; align-items: flex-start; height: 62px; }
  .contact__icon { width: 38px; height: 38px; flex: none; }
  .contact__text {
    margin-left: 25px; font-weight: 600; font-size: 17px; line-height: 21px; color: var(--navy);
  }
  .contact--phone .contact__text { padding-top: 8px; }
  .contact--web .contact__text { padding-top: 0; }
</style>
</head>
<body>

<section class="card card--front" aria-label="Card front">
  <svg class="card__shapes" viewBox="0 0 790 450" aria-hidden="true">
    <rect x="0" y="378" width="790" height="30" fill="var(--grey)"/>
    <path d="M0 365 H404 a6 6 0 0 1 6 6 V412 l-5 6 a6 6 0 0 1 -5 3 H0 Z" fill="var(--navy)"/>
    <path d="M249 376 H572 a4 4 0 0 1 3 6 L558 408 a4 4 0 0 1 -3 2 H249 a5 5 0 0 1 -5 -5 V381 a5 5 0 0 1 5 -5 Z" fill="var(--red)"/>
  </svg>
  <div class="wordmark">
    <span class="wordmark__name">Brelvan</span>
    <span class="wordmark__sub">Industries</span>
  </div>
  <div class="web-pill">www.brelvanindustries.com</div>
</section>

<section class="card card--back" aria-label="Card back">
  <svg class="card__shapes" viewBox="0 0 790 450" aria-hidden="true">
    <path d="M0 57 H418 a8 8 0 0 1 7 12 L387 140 a9 9 0 0 1 -8 4 H0 Z" fill="var(--red)"/>
    <path d="M0 52 H412 a8 8 0 0 1 7 12 L382 134 a9 9 0 0 1 -8 4 H0 Z" fill="var(--navy)"/>
    <rect x="0" y="380" width="480" height="37" fill="var(--grey)"/>
    <path d="M440 362 H790 V435 H425 a8 8 0 0 1 -8 -8 V400 L432 368 a10 10 0 0 1 8 -6 Z" fill="var(--navy)"/>
    <path d="M250 375 H621 a5 5 0 0 1 5 5 V417 a5 5 0 0 1 -5 5 H238 a5 5 0 0 1 -4 -7 L245 379 a6 6 0 0 1 5 -4 Z" fill="var(--red)"/>
  </svg>

  <div class="holder">
    <p class="holder__name">MARCUS <em>MARCUS</em></p>
    <p class="holder__role"><span class="holder__rule"></span><span class="holder__rule holder__rule--red"></span>YOUR DESIGNATION</p>
  </div>

  <ul class="contacts">
    <li class="contact contact--phone">
      <svg class="contact__icon" viewBox="0 0 38 38" aria-hidden="true">
        <circle cx="19" cy="19" r="19" fill="var(--red)"/>
        <path d="M13.5 11 l3 -1 l2.4 4.4 l-1.8 1.6 a9 9 0 0 0 4.6 4.6 l1.6 -1.8 l4.4 2.4 l-1 3 a3 3 0 0 1 -3.2 1.8 a15 15 0 0 1 -11.8 -11.8 a3 3 0 0 1 1.8 -3.2 Z" fill="var(--white)"/>
      </svg>
      <span class="contact__text">(253) 555-0174</span>
    </li>
    <li class="contact contact--web">
      <svg class="contact__icon" viewBox="0 0 38 38" aria-hidden="true">
        <circle cx="19" cy="19" r="19" fill="var(--red)"/>
        <g fill="none" stroke="var(--white)" stroke-width="1.3">
          <circle cx="19" cy="19" r="9"/>
          <ellipse cx="19" cy="19" rx="4" ry="9"/>
          <path d="M10 19 H28 M11.5 14.5 H26.5 M11.5 23.5 H26.5 M19 10 V28"/>
        </g>
      </svg>
      <span class="contact__text">marcus@kestrelbayholding.com<br>www.brelvanindustries.com</span>
    </li>
    <li class="contact contact--address">
      <svg class="contact__icon" viewBox="0 0 38 38" aria-hidden="true">
        <circle cx="19" cy="19" r="19" fill="var(--red)"/>
        <path d="M19 9.5 L29 18.5 H26 V28 H21.5 V22.5 H16.5 V28 H12 V18.5 H9 Z" fill="var(--white)"/>
      </svg>
      <span class="contact__text">61807 19th Street N,<br>Kent, WA 98517</span>
    </li>
  </ul>

  <div class="wordmark">
    <span class="wordmark__name">Brelvan</span>
    <span class="wordmark__sub">Industries</span>
  </div>
</section>

</body>
</html>
```